Chauffeur Car Driver Needing a design with/without logo for business cards

I'm a chauffeur car driver in Melbourne Australia. I have an extensive list of personal customers and need to provide a professional business card to new customers.
My business name is 'RidgeMark'.
I offer a personalised service to customer who need a transport alternative to taxis. I don't want it to look too 'upmarket' as i don't want it to seem too expensive or only for special occasions. The majority of my clients are business professionals who use me for airport transfers.
I definitely don't want the card/logo to have an image of a car/road etc. I prefer something abstract. A 'pencil-line'-type font will grab my attention but not absolutely necessary. Not too 'digital' or 'ultra - modern' looking.
I need the card to display the following information
Ridge Mark - main logo/text
Chauffeur Cars - sub text
Bruno Fellisar
0498 271 536
bookings@RidgeMark.com.au
I would like the focus to be on 'RidgeMark' with everything else smaller.
Look forward to seeing ideas!!!!
Target Market(s)
Business Corporate Professionals
Industry/Entity Type
Airport
Requirements
Nice to have
- Pencil line type font
Should not have
- Images of cars, road, tyres, steering wheel etc.

```html
<!DOCTYPE html>
<html lang="en">
<head>
<meta charset="utf-8">
<title>Ridge Mark – Chauffeur Cars business card</title>
<link rel="stylesheet" href="https://fonts.googleapis.com/css2?family=Arimo:wght@700&family=Poiret+One&display=swap">
<style>
  :root {
    --page-bg: #3a3836;
    --card-black: #0b0b0b;
    --leather-mid: #1a1a1a;
    --gold: #d6b869;
    --gold-muted: #9c8147;
    --gold-soft: #c4a55c;
  }
  * { margin: 0; padding: 0; box-sizing: border-box; }
  html, body {
    width: 1200px;
    height: 600px;
    overflow: hidden;
    background: var(--page-bg);
  }
  .canvas {
    position: relative;
    width: 1200px;
    height: 600px;
    display: flex;
    align-items: center;
    justify-content: center;
  }
  .business-card {
    position: relative;
    width: 900px;
    height: 514px;
    background: var(--card-black);
    overflow: hidden;
    box-shadow: 0 12px 30px rgba(0, 0, 0, 0.5);
  }
  .leather-texture {
    position: absolute;
    inset: 0;
    background: radial-gradient(ellipse at 45% 40%, var(--leather-mid) 0%, var(--card-black) 75%);
  }
  .brand-block {
    position: absolute;
    left: 110px;
    top: 120px;
    width: 680px;
  }
  .brand-name {
    font-family: "Poiret One", sans-serif;
    font-weight: 400;
    font-size: 124px;
    line-height: 1;
    letter-spacing: 2px;
    color: var(--gold);
    white-space: nowrap;
  }
  .brand-tagline {
    margin-top: 6px;
    margin-left: 250px;
    font-family: "Poiret One", sans-serif;
    font-size: 44px;
    letter-spacing: 2px;
    color: var(--gold-muted);
    white-space: nowrap;
  }
  .contact-row {
    position: absolute;
    left: 70px;
    bottom: 70px;
    display: flex;
    align-items: flex-end;
    gap: 34px;
  }
  .person-name {
    font-family: "Arimo", sans-serif;
    font-weight: 700;
    font-size: 32px;
    color: var(--gold-soft);
    white-space: nowrap;
  }
  .contact-details {
    list-style: none;
    margin-bottom: 40px;
    font-family: "Arimo", sans-serif;
    font-weight: 700;
    font-size: 22px;
    line-height: 1.2;
    color: var(--gold-soft);
    white-space: nowrap;
  }
</style>
</head>
<body>
  <main class="canvas">
    <article class="business-card">
      <div class="leather-texture" role="img" aria-label="Black tufted leather texture background"></div>
      <header class="brand-block">
        <h1 class="brand-name">Ridge Mark</h1>
        <p class="brand-tagline">chauffeur cars</p>
      </header>
      <footer class="contact-row">
        <p class="person-name">Bruno Fellisar</p>
        <ul class="contact-details">
          <li>P: 0498 271 536</li>
          <li>E: bookings@RidgeMark.com.au</li>
        </ul>
      </footer>
    </article>
  </main>
</body>
</html>
```